Bref créative
KORVO FREIGHT
BUSINESS CARDS AND BROCHURE LAYOUT
Professional
Reed Quandt
Owner/Specialist
I want no address
korvofreight@nubramail.com
www.korvofreight-example.com
just the logo on the back

```html
<!DOCTYPE html>
<html lang="en">
<head>
<meta charset="utf-8">
<title>Korvo Freight – Brochure and Stationery</title>
<link rel="stylesheet" href="https://fonts.googleapis.com/css2?family=Open+Sans:wght@400;700&family=Montserrat:wght@700;800&display=swap">
<style>
:root{
  --red:#d71920;
  --red-dark:#a50f15;
  --charcoal:#2f2f31;
  --grey:#8a8a8d;
  --light:#f4f4f4;
  --white:#ffffff;
  --ground:#e6e2dc;
  --photo-a:#c9ced4;
  --photo-b:#8d96a0;
}
*{box-sizing:border-box;margin:0;padding:0}
html,body{width:1200px;height:619px;overflow:hidden;background:var(--ground);font-family:"Open Sans",Arial,sans-serif;color:var(--charcoal)}
.canvas{position:relative;width:1200px;height:619px}
.piece{position:absolute;background:var(--white);box-shadow:0 3px 10px rgba(0,0,0,.25);overflow:hidden}
.page{position:absolute;top:0;bottom:0;overflow:hidden}
.swoosh{position:absolute;left:0;width:100%;display:block}
.photo{position:absolute;background:linear-gradient(160deg,var(--photo-a),var(--photo-b));border:1px solid var(--white)}
.brand{font-family:"Montserrat",Arial,sans-serif;font-weight:800;color:var(--red);letter-spacing:.5px;display:flex;align-items:center;gap:4px;white-space:nowrap}
.brand .dot{width:.8em;height:.8em;border-radius:50%;background:var(--red);display:inline-block}
.brand.on-red{color:var(--white)}
.brand.on-red .dot{background:var(--white)}
.heading{font-family:"Montserrat",Arial,sans-serif;font-weight:700;color:var(--red);font-size:7px;text-transform:uppercase;line-height:1.2}
.tab{display:inline-block;background:var(--red);color:var(--white);font-family:"Montserrat",Arial,sans-serif;font-weight:700;font-size:6px;padding:2px 6px;text-transform:uppercase}
.copy{font-size:4.6px;line-height:1.45;color:#555}
.copy.light{color:#fbe3e3}
.block{position:absolute}
</style>
</head>
<body>
<div class="canvas">

  <!-- Cover spread -->
  <section class="piece cover-spread" style="left:24px;top:84px;width:384px;height:222px">
    <div class="page back-cover" style="left:0;width:192px;background:var(--red)">
      <div class="photo" role="img" aria-label="Faint illustration of a delivery van" style="left:30px;top:50px;width:120px;height:70px;background:linear-gradient(160deg,#e0454b,#c3151b);border:none"></div>
      <svg class="swoosh" style="bottom:0;height:60px" viewBox="0 0 192 60" preserveAspectRatio="none"><path d="M0 30 Q96 0 192 22 L192 60 L0 60Z" fill="var(--charcoal)"/><path d="M0 40 Q96 12 192 32 L192 60 L0 60Z" fill="var(--white)"/></svg>
      <div class="copy block" style="left:10px;bottom:8px;color:var(--grey)">www.korvofreight-example.com</div>
    </div>
    <div class="page front-cover" style="left:192px;width:192px;background:var(--white)">
      <div style="position:absolute;left:0;top:0;width:100%;height:96px;background:var(--red)"></div>
      <div class="block" style="left:44px;top:38px">
        <div class="brand on-red" style="font-size:15px"><span class="dot"></span>KORVO FREIGHT</div>
        <div class="copy light" style="text-align:center;margin-top:2px">Reliable freight delivery</div>
      </div>
      <svg class="swoosh" style="top:84px;height:30px" viewBox="0 0 192 30" preserveAspectRatio="none"><path d="M0 0 L192 0 L192 10 Q96 34 0 14Z" fill="var(--red)"/><path d="M0 14 Q96 34 192 10 L192 16 Q96 40 0 20Z" fill="var(--charcoal)"/></svg>
      <div class="photo" role="img" aria-label="Photograph of white delivery vans outside a depot" style="left:0;top:108px;width:192px;height:90px;border:none"></div>
      <svg class="swoosh" style="bottom:0;height:32px" viewBox="0 0 192 32" preserveAspectRatio="none"><path d="M0 18 Q96 0 192 14 L192 32 L0 32Z" fill="var(--charcoal)"/><path d="M0 24 Q96 8 192 22 L192 32 L0 32Z" fill="var(--red)"/></svg>
    </div>
  </section>

  <!-- Inner spread -->
  <section class="piece inner-spread" style="left:426px;top:84px;width:306px;height:222px">
    <div class="page" style="left:0;width:153px;padding:12px 10px">
      <div class="heading">Flexible service for your business needs</div>
      <div class="photo" role="img" aria-label="Photograph of a loaded delivery van" style="position:relative;width:60px;height:38px;margin:5px 0;float:left;margin-right:5px"></div>
      <p class="copy">Fast regional freight with tracked pickups, careful handling and on-time drop-offs for every client.</p>
      <div class="heading" style="clear:both;padding-top:8px">Advanced freight planning with expert support</div>
      <div class="photo" role="img" aria-label="Photograph of a van parked at a loading dock" style="position:relative;width:70px;height:44px;margin:5px 0"></div>
      <p class="copy">Our fleet of vans covers city routes daily, so your parcels arrive safe and on schedule.</p>
      <div class="brand block" style="left:10px;bottom:10px;font-size:8px"><span class="dot"></span>KORVO FREIGHT</div>
    </div>
    <div class="page" style="left:153px;width:153px;padding:12px 10px;border-left:1px solid #e2e2e2">
      <div class="heading" style="text-align:right">Features</div>
      <p class="copy" style="margin-top:5px">We plan each load around your hours and keep you updated from dock to door.</p>
      <div class="photo" role="img" aria-label="Photograph of a driver loading parcels" style="position:relative;width:70px;height:44px;margin:8px 0"></div>
      <p class="copy">Fast regional freight with tracked pickups, careful handling and on-time drop-offs for every client.</p>
      <svg class="swoosh" style="bottom:0;height:26px" viewBox="0 0 153 26" preserveAspectRatio="none"><path d="M0 14 Q76 0 153 10 L153 26 L0 26Z" fill="var(--red)"/></svg>
    </div>
  </section>

  <!-- Tri-fold -->
  <section class="piece trifold" style="left:756px;top:84px;width:348px;height:210px">
    <div class="page" style="left:0;width:116px;padding:10px 8px">
      <div class="photo" role="img" aria-label="Photograph of a delivery truck on the road" style="left:0;top:0;width:116px;height:80px;border:none"></div>
      <div style="margin-top:86px"><span class="tab">About us</span></div>
      <p class="copy" style="margin-top:5px">Our fleet of vans covers city routes daily, so your parcels arrive safe and on schedule.</p>
    </div>
    <div class="page" style="left:116px;width:116px;padding:10px 8px;background:var(--light)">
      <svg class="swoosh" style="top:0;height:40px" viewBox="0 0 116 40" preserveAspectRatio="none"><path d="M0 0 L116 0 L116 18 Q58 40 0 22Z" fill="var(--red)"/><path d="M0 22 Q58 40 116 18 L116 24 Q58 46 0 28Z" fill="var(--charcoal)"/></svg>
      <div class="photo" role="img" aria-label="Photograph of vans lined up" style="left:14px;top:60px;width:88px;height:54px"></div>
      <div class="brand block" style="left:14px;top:130px;font-size:8px"><span class="dot"></span>KORVO FREIGHT</div>
      <svg class="swoosh" style="bottom:0;height:30px" viewBox="0 0 116 30" preserveAspectRatio="none"><path d="M0 16 Q58 0 116 12 L116 30 L0 30Z" fill="var(--red)"/></svg>
    </div>
    <div class="page" style="left:232px;width:116px;padding:10px 8px">
      <div class="heading">Assignment &amp; business</div>
      <p class="copy" style="margin-top:5px">We plan each load around your hours and keep you updated from dock to door.</p>
      <div style="margin-top:10px"><span class="tab">Features</span></div>
      <p class="copy" style="margin-top:5px">Fast regional freight with tracked pickups, careful handling and on-time drop-offs for every client.</p>
      <svg class="swoosh" style="bottom:0;height:30px" viewBox="0 0 116 30" preserveAspectRatio="none"><path d="M0 12 Q58 0 116 16 L116 30 L0 30Z" fill="var(--charcoal)"/><path d="M0 20 Q58 8 116 24 L116 30 L0 30Z" fill="var(--red)"/></svg>
    </div>
  </section>

  <!-- Bottom spread one -->
  <section class="piece services-spread" style="left:24px;top:330px;width:312px;height:216px">
    <div class="page" style="left:0;width:156px;padding:10px 8px">
      <div class="photo" role="img" aria-label="Photograph of a truck driving on a highway" style="left:0;top:0;width:156px;height:100px;border:none"></div>
      <div style="margin-top:108px"><span class="tab">Services</span></div>
      <p class="copy" style="margin-top:5px">Our fleet of vans covers city routes daily, so your parcels arrive safe and on schedule.</p>
      <svg class="swoosh" style="bottom:0;height:26px" viewBox="0 0 156 26" preserveAspectRatio="none"><path d="M0 14 Q78 0 156 10 L156 26 L0 26Z" fill="var(--red)"/></svg>
    </div>
    <div class="page" style="left:156px;width:156px">
      <svg class="swoosh" style="top:0;height:70px" viewBox="0 0 156 70" preserveAspectRatio="none"><path d="M0 0 L156 0 L156 40 Q78 72 0 46Z" fill="var(--red)"/><path d="M0 46 Q78 72 156 40 L156 48 Q78 80 0 54Z" fill="var(--charcoal)"/></svg>
      <div class="brand block" style="left:30px;top:96px;font-size:10px"><span class="dot"></span>KORVO FREIGHT</div>
      <div class="photo" role="img" aria-label="Illustration of stacked cardboard boxes" style="left:50px;top:124px;width:60px;height:60px;background:linear-gradient(160deg,#c89a63,#8f6435);border:none"></div>
    </div>
  </section>

  <!-- Bottom spread two -->
  <section class="piece assignment-spread" style="left:354px;top:330px;width:330px;height:216px">
    <div class="page" style="left:0;width:165px;padding:12px 10px">
      <svg class="swoosh" style="top:0;height:28px" viewBox="0 0 165 28" preserveAspectRatio="none"><path d="M0 0 L165 0 L165 12 Q82 30 0 16Z" fill="var(--red)"/></svg>
      <div class="heading" style="margin-top:24px">Assignment &amp; business</div>
      <p class="copy" style="margin-top:5px">We plan each load around your hours and keep you updated from dock to door.</p>
      <div class="photo" role="img" aria-label="Photograph of a van at a warehouse" style="position:relative;width:80px;height:48px;margin-top:8px"></div>
      <div class="brand block" style="left:10px;bottom:10px;font-size:8px"><span class="dot"></span>KORVO FREIGHT</div>
    </div>
    <div class="page" style="left:165px;width:165px;padding:12px 10px;border-left:1px solid #e2e2e2">
      <svg class="swoosh" style="top:0;height:28px" viewBox="0 0 165 28" preserveAspectRatio="none"><path d="M0 0 L165 0 L165 16 Q82 30 0 12Z" fill="var(--charcoal)"/></svg>
      <div style="margin-top:24px"><span class="tab">Features</span></div>
      <p class="copy" style="margin-top:5px">Fast regional freight with tracked pickups, careful handling and on-time drop-offs for every client.</p>
      <div class="photo" role="img" aria-label="Photograph of parcels being unloaded" style="position:relative;width:80px;height:48px;margin-top:8px"></div>
      <svg class="swoosh" style="bottom:0;height:26px" viewBox="0 0 165 26" preserveAspectRatio="none"><path d="M0 14 Q82 0 165 10 L165 26 L0 26Z" fill="var(--red)"/></svg>
    </div>
  </section>

  <!-- Letterhead -->
  <section class="piece letterhead" style="left:702px;top:330px;width:120px;height:200px;padding:14px 10px">
    <div class="brand" style="font-size:8px"><span class="dot"></span>KORVO FREIGHT</div>
    <p class="copy" style="margin-top:18px">Dear Client, thank you for choosing our freight team.</p>
    <div style="margin-top:8px;height:60px;background:repeating-linear-gradient(var(--white) 0 5px,#e5e5e5 5px 6px)"></div>
    <svg class="swoosh" style="bottom:0;height:24px" viewBox="0 0 120 24" preserveAspectRatio="none"><path d="M0 10 Q60 0 120 8 L120 24 L0 24Z" fill="var(--charcoal)"/><path d="M0 16 Q60 6 120 14 L120 24 L0 24Z" fill="var(--red)"/></svg>
  </section>

  <!-- Envelope -->
  <section class="piece envelope" style="left:842px;top:320px;width:244px;height:104px;padding:12px 12px">
    <div class="brand" style="font-size:9px"><span class="dot"></span>KORVO FREIGHT</div>
    <div class="copy" style="margin-top:3px">www.korvofreight-example.com</div>
    <svg class="swoosh" style="bottom:0;height:34px" viewBox="0 0 244 34" preserveAspectRatio="none"><path d="M0 14 Q122 0 244 10 L244 34 L0 34Z" fill="var(--charcoal)"/><path d="M0 20 Q122 6 244 18 L244 34 L0 34Z" fill="var(--red)"/></svg>
  </section>

  <!-- Business cards -->
  <section class="piece card card-front" style="left:842px;top:444px;width:168px;height:96px;padding:10px 10px">
    <div class="brand" style="font-size:9px"><span class="dot"></span>KORVO FREIGHT</div>
    <div style="font-family:'Montserrat',Arial,sans-serif;font-weight:700;font-size:8px;margin-top:8px">Reed Quandt</div>
    <div class="copy" style="font-size:5.5px">Owner/Specialist</div>
    <div class="copy" style="font-size:5.5px;margin-top:4px">korvofreight@nubramail.com</div>
    <div class="copy" style="font-size:5.5px">www.korvofreight-example.com</div>
    <svg class="swoosh" style="bottom:0;height:18px" viewBox="0 0 168 18" preserveAspectRatio="none"><path d="M0 8 Q84 0 168 6 L168 18 L0 18Z" fill="var(--red)"/></svg>
  </section>
  <section class="piece card card-back" style="left:1024px;top:444px;width:168px;height:96px;background:var(--red);display:flex;align-items:center;justify-content:center">
    <svg class="swoosh" style="bottom:0;height:24px" viewBox="0 0 168 24" preserveAspectRatio="none"><path d="M0 12 Q84 0 168 10 L168 24 L0 24Z" fill="var(--charcoal)"/></svg>
    <div class="brand on-red" style="font-size:11px;position:relative"><span class="dot"></span>KORVO FREIGHT</div>
  </section>

</div>
</body>
</html>
```